Velter Labs - Mushroom Supplement Packaging

Our brand is called Velter Labs. I've added a couple different logos that you can use. We are creating a line up of Mushroom Supplement products. I will add the entire line-up of products here. I've added examples of other products and packaging shape types I can purchase. Give me different options for packaging that is minimalist and clean for this brand that makes it look really well made and clean and make people want to buy.

Product 1 Lions Mane 1g
Product 2 Cordyceps 1g
Product 3 Chaga 1g
Product 4 Turkey Tail 1g
Product 5 Reishi 1g
Product 6 Maitake 1g
Product 7 Shiitake 1g

Product 8 (Mix) Lions Mane 143mg
Cordyceps 143mg
Chaga 143mg
Turkey Tail 143mg
Reishi 143mg
Maitake 143mg
Shiitake 143mg

```html
<!DOCTYPE html>
<html lang="en">
<head>
<meta charset="utf-8">
<title>Velter Labs – Lion's Mane Mushroom Supplement Label</title>
<link rel="stylesheet" href="https://fonts.googleapis.com/css2?family=Montserrat:wght@400;500&family=Oswald:wght@500;600&display=swap">
<style>
  :root {
    --page-bg: #ececec;
    --label-dark: #262626;
    --label-mid: #3b3b3b;
    --text-white: #ffffff;
    --text-muted: #9a9a9a;
    --rule: #8a8a8a;
    --dose-bg: #8c8c8c;
    --dose-text: #2a2a2a;
    --art-tone: #4a4a4a;
  }
  * { margin: 0; padding: 0; box-sizing: border-box; }
  html, body {
    width: 1200px; height: 1132px; overflow: hidden;
    background: var(--page-bg);
  }
  .label {
    position: absolute; left: 120px; top: 101px;
    width: 960px; height: 930px;
    background: linear-gradient(90deg, var(--label-dark) 0%, var(--label-mid) 45%, var(--label-dark) 100%);
    overflow: hidden;
  }
  .mane-art {
    position: absolute; left: 0; top: 10px;
    width: 430px; height: 880px;
    background: radial-gradient(ellipse 60% 55% at 35% 50%, var(--art-tone) 0%, rgba(74,74,74,0.35) 55%, rgba(74,74,74,0) 80%);
    opacity: 0.7;
  }
  .brand {
    position: absolute; left: 368px; top: 42px;
    font-family: "Oswald", sans-serif; font-weight: 500;
    color: var(--text-white);
    text-transform: uppercase; line-height: 0.95;
  }
  .brand-name { display: block; font-size: 62px; letter-spacing: 1px; }
  .brand-sub { display: block; font-size: 40px; letter-spacing: 10px; padding-left: 30px; }
  .dose {
    position: absolute; left: 774px; top: 0;
    width: 165px; height: 152px;
    background: var(--dose-bg); color: var(--dose-text);
    font-family: "Montserrat", sans-serif; text-align: center;
  }
  .dose-value { display: block; font-family: "Oswald", sans-serif; font-weight: 600; font-size: 70px; line-height: 1; padding-top: 12px; }
  .dose-unit { display: block; font-size: 28px; font-weight: 500; margin-top: 6px; }
  .product-type {
    position: absolute; left: 388px; top: 326px;
    font-family: "Montserrat", sans-serif; font-weight: 500;
    font-size: 66px; line-height: 1.0; letter-spacing: 2px;
    color: var(--text-white); text-transform: uppercase;
    background: linear-gradient(90deg, #ffffff 60%, #a5a5a5 100%);
    -webkit-background-clip: text; background-clip: text; color: transparent;
  }
  .divider {
    position: absolute; left: 390px; top: 488px;
    width: 514px; height: 2px; background: var(--rule);
  }
  .benefits {
    position: absolute; left: 390px; top: 502px;
    list-style: none;
    font-family: "Montserrat", sans-serif; font-weight: 400;
    font-size: 18px; line-height: 33px; letter-spacing: 1.5px;
    color: var(--text-muted); text-transform: uppercase;
  }
  .product-name { position: absolute; left: 54px; top: 672px; width: 860px; height: 232px; }
</style>
</head>
<body>
  <main class="label">
    <div class="mane-art" role="img" aria-label="Faint line illustration of a lion's mane in dark grey"></div>

    <div class="brand">
      <span class="brand-name">Velter</span>
      <span class="brand-sub">Labs</span>
    </div>

    <div class="dose">
      <span class="dose-value">1</span>
      <span class="dose-unit">MG</span>
    </div>

    <h2 class="product-type">Mushroom<br>Supplement</h2>
    <div class="divider"></div>

    <ul class="benefits">
      <li>Supports a healthy immune system</li>
      <li>Supports overall well-being</li>
      <li>Brain booster</li>
    </ul>

    <svg class="product-name" viewBox="0 0 860 232" aria-label="Lion's Mane">
      <defs>
        <linearGradient id="name-fade" x1="0" y1="0" x2="1" y2="0">
          <stop offset="0" stop-color="#ffffff"/>
          <stop offset="0.6" stop-color="#e6e6e6"/>
          <stop offset="1" stop-color="#8e8e8e"/>
        </linearGradient>
      </defs>
      <text x="0" y="226" textLength="858" lengthAdjust="spacingAndGlyphs"
            font-family="Oswald, sans-serif" font-weight="600" font-size="290"
            fill="url(#name-fade)">LION'S MANE</text>
    </svg>
  </main>
</body>
</html>
```